Letterhead Design Project (logo provided)

We are a legal services provider company called VRN Legal based in the UK and would like some letterhead paper designed.

The design should use the attached logo, and should use the colors feature in the logo (along with blacks and/or greys).

The background paper must be white - and A4 size.

The letterhead should be provided in both .pdf and .doc (or .odf) formats.

Target Market(s)

Customers and clients for legal services

Industry/Entity Type

Legal

Requirements
Must have
• The header must include the following information:

Business name - VRN Legal LLP
Office address - Larchmead Court, Brackford, Westshire BK4 4TL, United Kingdom
Telephone - +44 (0)1632 960480
Email - mail@ [domain given below]
Website: www.vrnlegal-example.com

The footer must include the following information:

Registered office address - 14 Alder Row, Brindlecote, Brackford, Westshire BK4 6QD, United Kingdom
Companies House registration number - OC718463
VAT registration number - GB 417386205

```html
<!DOCTYPE html>
<html lang="en">
<head>
<meta charset="utf-8">
<title>VRN Legal Letterhead</title>
<link rel="stylesheet" href="https://fonts.googleapis.com/css2?family=Fira+Sans:wght@300;400&display=swap">
<style>
  :root {
    --backdrop: #fdfbf4;
    --paper: #ffffff;
    --paper-edge: #ecebe4;
    --brand-blue: #2b5da8;
    --brand-green: #34a94a;
    --text-grey: #9a9a9a;
  }
  * { margin: 0; padding: 0; box-sizing: border-box; }
  html, body {
    width: 1200px; height: 1000px; overflow: hidden;
    background: var(--backdrop);
    font-family: "Fira Sans", Arial, sans-serif;
  }
  .letterhead {
    position: absolute; left: 295px; top: 72px;
    width: 595px; height: 841px;
    background: var(--paper);
    border: 1px solid var(--paper-edge);
  }
  .accent-band {
    position: absolute; left: 276px; top: 0;
    width: 318px; height: 14px;
    background: var(--brand-green);
  }
  .brand-name {
    position: absolute; left: 29px; top: 27px;
    font-size: 44px; font-weight: 400; letter-spacing: 0.3px;
    text-transform: uppercase;
    color: var(--brand-blue);
    line-height: 1;
    white-space: nowrap;
  }
  .contact {
    position: absolute; top: 34px;
    font-size: 7.4px; line-height: 10.2px; font-weight: 400;
  }
  .contact-company { left: 275px; }
  .contact-reach { left: 425px; }
  .contact-row { display: flex; }
  .label { flex: none; white-space: nowrap; }
  .contact-company .label { width: 56px; }
  .contact-reach .label { width: 40px; }
  .value { color: var(--text-grey); font-weight: 300; }
  .value::before { content: "· "; }
  .contact-company .value { width: 92px; }
  .contact-reach .value { white-space: nowrap; }
  .blue { color: var(--brand-blue); }
  .green { color: var(--brand-green); }
  .legal-footer {
    position: absolute; left: 32px; top: 769px;
    font-size: 9.6px; line-height: 15px; font-weight: 300;
  }
  .legal-footer .label { width: 170px; font-weight: 400; }
  .legal-footer .value { white-space: nowrap; }
</style>
</head>
<body>
  <main class="letterhead">
    <div class="accent-band"></div>

    <header>
      <div class="brand-name">VRN Legal</div>

      <dl class="contact contact-company">
        <div class="contact-row"><dt class="label blue">Business name</dt><dd class="value">VRN Legal LLP</dd></div>
        <div class="contact-row"><dt class="label green">Office address</dt><dd class="value">Larchmead Court, Brackford, Westshire BK4 4TL, United Kingdom</dd></div>
      </dl>

      <dl class="contact contact-reach">
        <div class="contact-row"><dt class="label blue">Telephone</dt><dd class="value">+44 (0)1632 960480</dd></div>
        <div class="contact-row"><dt class="label green">Email</dt><dd class="value">mail@ (domain given below)</dd></div>
        <div class="contact-row"><dt class="label blue">Website</dt><dd class="value">www.vrnlegal-example.com</dd></div>
      </dl>
    </header>

    <footer>
      <dl class="legal-footer">
        <div class="contact-row"><dt class="label blue">Registered office address</dt><dd class="value">14 Alder Row, Brindlecote, Brackford, Westshire BK4 6QD, United Kingdom</dd></div>
        <div class="contact-row"><dt class="label green">Companies House registration number</dt><dd class="value">OC718463</dd></div>
        <div class="contact-row"><dt class="label blue">VAT registration number</dt><dd class="value">GB 417386205</dd></div>
      </dl>
    </footer>
  </main>
</body>
</html>
```